Business Card needed for International Migration and Education business

we are based in Australia, the business is called 'FarReach Relocation' and its sister business for international education is called 'FarReach Learning' - we need the design for the business 'FarReach Relocation' - FarReach Relocation is about migration to Australia (but not limited to Australia only therefore purely Australian look would not fit). We would like to see designs that use the color blue or acqua and maybe orange..all those colours don't have to be used together and not only those colours are to be used. We are looking for a modern design. The final design should communicate modern thinking, professionalism, dynamism, confidence. We would like to use the same business card design for our sister business "FarReach Learning" - which is business about studying in different countries as we recruit students to study in Australia, USA, New Zealand, Canada, UK etc. We would like to be able the final design to be easily changed by us to fit the 'FarReach Learning' business - we would only change the contact text (email address etc)

The information to be included in the business card: Tessa Virnaud Managing Director Migration Agent MARN 0917264 FarReach Relocation postal address: PO Box 2749, Carlwood East VIC 3179, Australia mobile: 0417296031 office address: Level 1, 287 Fenwick Road, Ardmere VIC 3211 web www.farreachrelocation-example.com telephone: 61 3 8714 6023 fax + 61 3 8735 2910 email: tessa@farreachrelocation-example.com

```html
<!DOCTYPE html>
<html lang="en">
<head>
<meta charset="utf-8">
<title>FarReach Relocation – Business Card</title>
<link rel="stylesheet" href="https://fonts.googleapis.com/css2?family=Didact+Gothic&family=Montserrat:wght@300;700&display=swap">
<style>
  :root {
    --page-bg: #e9e9e9;
    --card-white: #ffffff;
    --band-blue: #00b9ef;
    --accent-orange: #f7941d;
    --ink: #3a3a3a;
    --ink-dark: #232323;
    --map-light: #e6ebf1;
    --map-mid: #c9d2de;
  }
  * { margin: 0; padding: 0; box-sizing: border-box; }
  html, body {
    width: 1200px;
    height: 1200px;
    overflow: hidden;
    background: var(--page-bg);
  }
  .card {
    position: absolute;
    left: 80px;
    top: 290px;
    width: 1040px;
    height: 620px;
    background: var(--card-white);
    overflow: hidden;
    box-shadow: 0 6px 18px rgba(0,0,0,0.18);
    font-family: "Didact Gothic", "Century Gothic", sans-serif;
    color: var(--ink);
  }
  .world-map {
    position: absolute;
    left: 0;
    top: 22px;
    width: 1000px;
    height: 430px;
    border-radius: 40px;
    background: radial-gradient(ellipse at 50% 45%, var(--map-mid) 0%, var(--map-light) 60%, rgba(255,255,255,0) 85%);
    opacity: 0.85;
  }
  .brand-bar {
    position: absolute;
    left: 885px;
    top: 92px;
    width: 155px;
    height: 70px;
    background: var(--accent-orange);
  }
  .brand-name {
    position: absolute;
    right: 180px;
    top: 150px;
    font-size: 44px;
    color: var(--ink);
    letter-spacing: 0.5px;
    white-space: nowrap;
  }
  .name-marker {
    position: absolute;
    left: 0;
    top: 352px;
    width: 62px;
    height: 72px;
    background: var(--accent-orange);
  }
  .person {
    position: absolute;
    left: 76px;
    top: 348px;
  }
  .person-name {
    font-family: "Montserrat", "Century Gothic", sans-serif;
    font-weight: 300;
    font-size: 30px;
    color: var(--ink-dark);
    letter-spacing: 0.5px;
    text-transform: uppercase;
    white-space: nowrap;
  }
  .person-name .surname { font-weight: 700; }
  .person-role {
    font-size: 22px;
    font-style: italic;
    color: var(--ink);
    margin-top: 2px;
    white-space: nowrap;
  }
  .contact-band {
    position: absolute;
    left: 0;
    top: 448px;
    width: 1040px;
    height: 172px;
    background: var(--band-blue);
  }
  .divider {
    position: absolute;
    width: 2px;
    background: var(--ink-dark);
  }
  .contact-col {
    position: absolute;
    font-size: 20px;
    line-height: 1.3;
    color: var(--ink-dark);
  }
  .contact-row {
    display: flex;
    align-items: flex-start;
    gap: 16px;
    margin-bottom: 14px;
    white-space: nowrap;
  }
  .contact-row svg {
    flex: 0 0 auto;
    width: 26px;
    height: 26px;
    fill: var(--ink-dark);
    margin-top: 2px;
  }
  .col-address .contact-row { gap: 14px; margin-bottom: 6px; font-size: 19px; }
</style>
</head>
<body>
  <div class="card">
    <div class="world-map" role="img" aria-label="Dotted world map in soft grey-blue spanning the card"></div>

    <div class="brand-bar"></div>
    <div class="brand-name">FarReach Relocation</div>

    <div class="name-marker"></div>
    <div class="person">
      <div class="person-name">Tessa <span class="surname">Virnaud</span></div>
      <div class="person-role">Managing Director Migration Agent MARN 0917264</div>
    </div>

    <div class="contact-band"></div>

    <div class="divider" style="left:62px; top:478px; height:122px;"></div>
    <div class="divider" style="left:300px; top:462px; height:122px;"></div>
    <div class="divider" style="left:618px; top:452px; height:110px;"></div>

    <div class="contact-col col-phone" style="left:78px; top:490px;">
      <div class="contact-row">
        <svg viewBox="0 0 24 24" aria-hidden="true"><path d="M6.6 10.8a15.1 15.1 0 0 0 6.6 6.6l2.2-2.2a1 1 0 0 1 1-.25 11.4 11.4 0 0 0 3.6.57 1 1 0 0 1 1 1V20a1 1 0 0 1-1 1A17 17 0 0 1 3 4a1 1 0 0 1 1-1h3.5a1 1 0 0 1 1 1c0 1.25.2 2.45.57 3.57a1 1 0 0 1-.25 1z"/></svg>
        <span>61 3 8714 6023</span>
      </div>
      <div class="contact-row">
        <svg viewBox="0 0 24 24" aria-hidden="true"><path d="M7 1h10a2 2 0 0 1 2 2v18a2 2 0 0 1-2 2H7a2 2 0 0 1-2-2V3a2 2 0 0 1 2-2zm0 3v15h10V4zm5 16.2a.9.9 0 1 0 0 1.8.9.9 0 0 0 0-1.8z"/></svg>
        <span>0417296031</span>
      </div>
    </div>

    <div class="contact-col col-fax" style="left:318px; top:470px;">
      <div class="contact-row">
        <svg viewBox="0 0 24 24" aria-hidden="true"><path d="M6 2h12v5H6zM4 8h16a2 2 0 0 1 2 2v7h-4v5H6v-5H2v-7a2 2 0 0 1 2-2zm4 8v4h8v-4zm10-5.5a1 1 0 1 0 0 2 1 1 0 0 0 0-2z"/></svg>
        <span>+ 61 3 8735 2910</span>
      </div>
      <div class="contact-row">
        <svg viewBox="0 0 24 24" aria-hidden="true"><path d="M2 5h20v14H2zm2 2v.4l8 5.2 8-5.2V7zm0 2.8V17h16V9.8l-8 5.2z"/></svg>
        <span>PO Box 2749,<br>Carlwood East VIC 3179</span>
      </div>
    </div>

    <div class="contact-col col-address" style="left:634px; top:456px;">
      <div class="contact-row">
        <svg viewBox="0 0 24 24" aria-hidden="true"><path d="M12 2a7 7 0 0 0-7 7c0 5.2 7 13 7 13s7-7.8 7-13a7 7 0 0 0-7-7zm0 9.5a2.5 2.5 0 1 1 0-5 2.5 2.5 0 0 1 0 5z"/></svg>
        <span>Level 1, 287 Fenwick Road,<br>Ardmere VIC 3211</span>
      </div>
      <div class="contact-row">
        <svg viewBox="0 0 24 24" aria-hidden="true"><path d="M12 2a10 10 0 1 0 0 20 10 10 0 0 0 0-20zm6.9 6h-2.9a15.6 15.6 0 0 0-1.4-3.6A8 8 0 0 1 18.9 8zM12 4c.8 1.2 1.5 2.5 1.9 4h-3.8c.4-1.5 1.1-2.8 1.9-4zM4.3 14a8 8 0 0 1 0-4h3.3a16 16 0 0 0 0 4zm.8 2h2.9c.3 1.3.8 2.5 1.4 3.6A8 8 0 0 1 5.1 16zM8 8H5.1a8 8 0 0 1 4.3-3.6C8.8 5.5 8.3 6.7 8 8zm4 12c-.8-1.2-1.5-2.5-1.9-4h3.8c-.4 1.5-1.1 2.8-1.9 4zm2.3-6H9.7a14 14 0 0 1 0-4h4.6a14 14 0 0 1 0 4zm.3 5.6c.6-1.1 1.1-2.3 1.4-3.6h2.9a8 8 0 0 1-4.3 3.6zm1.8-5.6a16 16 0 0 0 0-4h3.3a8 8 0 0 1 0 4z"/></svg>
        <span>www.farreachrelocation-example.com<br>tessa@farreachrelocation-example.com</span>
      </div>
    </div>
  </div>
</body>
</html>
```